Kestrel Summit 2019 Enemies of the End-Times Church Flyer

We want a church conference flyer designed. We are looking for a professional, yet catchy design that uses our brand colors and logo creatively while communicating key information of the event effectively. <br/>The flyer must include all of the following:<br/>Title: Kestrel Summit 2019<br/>Topic: The Enemies of The End-Times Church <br/>Subtitles: <br/> -How the antichrist raises an army by social behavior engineering. <br/>-How the architects of modern social constructs escaped the church's radar. <br/>-The Holy Spirit's end-times agenda:<br/> The Knock-Out Punch!<br/>Speaker: Prophet Marcus Toliver <br/>Dates/time: December 27, 28 & 29 at 6pm<br/>Location: Halvorn Community Center <br/> 241 Pellham Street <br/> Portland, ME 04102<br/>Contact info: phone: 207-555-0148 <br/>email: contact@brookmeadow.example <br/> www.vutel.example<br/>*The flyer must also include a picture of the speaker and our Vutel logo <br/>Thanks, we look forward to seeing what you come up with!

Colors

Designer to choose colors to be used in the design.

Requirements
Must have
• The flyer must include all of the following:
• Title: Kestrel Summit 2019
• Topic: The Enemies of The End-Times Church
• Subtitles:
• -How the antichrist raises an army by social behavior engineering.
• -How the architects of modern social constructs escaped the church's radar.
• -The Holy Spirit's end-times agenda:
• The Knock-Out Punch!
• Speaker: Prophet Marcus Toliver
• Dates/time: December 27, 28 & 29 at 6pm
• Location: Halvorn Community Center
• 241 Pellham Street
• Portland, ME 04102
• Contact info: phone: 207-555-0148
• email: contact@brookmeadow.example
• www.vutel.example
• *The flyer must also include a picture of the speaker and our Vutel logo
Should not have
• Pictures of crosses or church buildings

```html
<!DOCTYPE html>
<html lang="en">
<head>
<meta charset="utf-8">
<title>Kestrel Summit 2019 — The Enemies of the End-Times Church</title>
<link rel="stylesheet" href="https://fonts.googleapis.com/css2?family=Cinzel:wght@700&family=Crimson+Text:wght@600;700&family=Noto+Sans:wght@700&family=Archivo+Black&family=Montserrat:wght@500;700&display=swap">
<style>
  :root {
    --navy: #0c2f50;
    --navy-deep: #021f37;
    --orange: #f7941d;
    --bronze: #b5651d;
    --paper: #ffffff;
    --mist: #e8eef3;
    --name-panel: #eaf5f8;
  }
  * { margin: 0; padding: 0; box-sizing: border-box; }
  html, body { width: 785px; height: 1200px; overflow: hidden; background: var(--paper); }
  .flyer { position: relative; width: 785px; height: 1200px; overflow: hidden;
    background: linear-gradient(180deg, #f4f7fa 0%, var(--mist) 30%, #f3f6f9 60%, #fff 100%); }
  .shapes { position: absolute; inset: 0; }

  .brand { position: absolute; top: 52px; left: 0; width: 100%; display: flex; justify-content: center; align-items: center; gap: 10px; }
  .brand-dot { width: 16px; height: 16px; border-radius: 50%; background: var(--orange); }
  .brand-name { font-family: "Crimson Text", serif; font-weight: 600; font-size: 50px; line-height: 1; color: var(--navy); letter-spacing: 1px; }

  .title { position: absolute; top: 132px; width: 100%; text-align: center; font-family: "Cinzel", serif; font-weight: 700; font-size: 41px; color: var(--navy); letter-spacing: 1px; }
  .topic { position: absolute; top: 188px; width: 100%; text-align: center; font-family: "Crimson Text", serif; font-weight: 700; font-size: 23px; color: var(--orange); letter-spacing: 0.3px; }
  .points { position: absolute; top: 248px; width: 100%; text-align: center; font-family: "Noto Sans", sans-serif; font-weight: 700; font-size: 16px; line-height: 23px; color: var(--navy); letter-spacing: 0.6px; }

  .agenda { position: absolute; left: 300px; top: 388px; width: 462px; text-align: right; transform: rotate(2.4deg); transform-origin: right center;
    font-family: "Noto Sans", sans-serif; font-weight: 700; font-size: 21px; line-height: 38px; color: var(--paper); letter-spacing: 0.6px; }

  .speaker-photo { position: absolute; left: 39px; top: 429px; width: 224px; height: 224px; border-radius: 50%; border: 6px solid var(--orange);
    background: radial-gradient(circle at 45% 40%, #6b4a36 0%, #6b4a36 22%, #a9997a 45%, #b8c3d8 80%); }
  .speaker-panel { position: absolute; left: 252px; top: 498px; width: 496px; height: 84px; border-radius: 22px; border: 5px solid var(--orange);
    background: var(--name-panel); display: flex; align-items: center; justify-content: center; padding-left: 18px; }
  .speaker-name { font-family: "Cinzel", serif; font-weight: 700; font-size: 28px; color: var(--navy); letter-spacing: 0.5px; }

  .date { position: absolute; top: 697px; width: 154px; height: 154px; border-radius: 50%;
    background: linear-gradient(135deg, #ffffff 0%, #9a9ea4 35%, #f5f5f5 55%, #8d9096 80%, #ffffff 100%); display: flex; align-items: center; justify-content: center; }
  .date-ring { width: 136px; height: 136px; border-radius: 50%; background: var(--navy-deep); display: flex; align-items: center; justify-content: center; }
  .date-face { width: 124px; height: 124px; border-radius: 50%; background: linear-gradient(135deg, #ffffff 0%, #d8dadd 45%, #ffffff 70%, #c7c9cc 100%);
    display: flex; flex-direction: column; align-items: center; justify-content: center; }
  .date-day { font-family: "Crimson Text", serif; font-weight: 700; font-size: 70px; line-height: 56px; color: #0b1620; letter-spacing: -2px; }
  .date-month { font-family: "Crimson Text", serif; font-weight: 700; font-size: 15px; color: var(--bronze); margin-top: 4px; }
  .date-27 { left: 142px; } .date-28 { left: 326px; } .date-29 { left: 533px; }

  .time { position: absolute; top: 860px; width: 100%; text-align: center; padding-right: 14px; font-family: "Archivo Black", sans-serif; font-size: 37px;
    color: var(--orange); -webkit-text-stroke: 2px #fff; paint-order: stroke fill; letter-spacing: 0.5px; }

  .venue { position: absolute; left: 225px; top: 927px; width: 348px; height: 130px; border: 6px solid var(--orange); border-radius: 10px; background: #f8fbfc;
    text-align: center; font-family: "Montserrat", sans-serif; padding-top: 12px; }
  .venue-label { font-weight: 700; font-size: 20px; color: var(--orange); letter-spacing: 0.5px; line-height: 26px; }
  .venue-address { font-weight: 500; font-size: 15px; line-height: 22px; color: var(--navy-deep); letter-spacing: 0.3px; }

  .contact { position: absolute; left: 0; top: 1115px; width: 785px; height: 85px; display: flex; font-family: "Montserrat", sans-serif; font-weight: 700; }
  .contact-item { display: flex; align-items: center; justify-content: center; }
  .contact-phone { width: 230px; color: var(--orange); font-size: 21px; }
  .contact-email { width: 333px; background: var(--orange); color: #fff; font-size: 17px; }
  .contact-web { width: 222px; color: var(--orange); font-size: 20px; }
</style>
</head>
<body>
<main class="flyer">
  <svg class="shapes" width="785" height="1200" viewBox="0 0 785 1200" aria-hidden="true">
    <polygon points="0,474 785,325 785,1115 0,1115" fill="var(--navy-deep)"/>
    <polygon points="292,362 785,398 785,487 267,472" fill="var(--orange)"/>
  </svg>

  <header class="brand">
    <span class="brand-dot"></span>
    <span class="brand-name">VUTEL</span>
  </header>

  <h1 class="title">Kestrel Summit 2019</h1>
  <h2 class="topic">THE ENEMIES OF THE END-TIMES CHURCH</h2>
  <p class="points">How the antichrist raises an army by social<br>behavior engineering.<br>How the architects of modern social constructs<br>escaped the church's radar.</p>

  <p class="agenda">The Holy Spirit's end-times agenda:<br>The Knock-Out Punch!</p>

  <div class="speaker-photo" role="img" aria-label="Photo of the speaker, Prophet Marcus Toliver, preaching with a headset microphone"></div>
  <div class="speaker-panel"><span class="speaker-name">Prophet Marcus Toliver</span></div>

  <div class="date date-27"><div class="date-ring"><div class="date-face"><span class="date-day">27</span><span class="date-month">DECEMBER</span></div></div></div>
  <div class="date date-28"><div class="date-ring"><div class="date-face"><span class="date-day">28</span><span class="date-month">DECEMBER</span></div></div></div>
  <div class="date date-29"><div class="date-ring"><div class="date-face"><span class="date-day">29</span><span class="date-month">DECEMBER</span></div></div></div>

  <p class="time">FROM 6:00 P.M</p>

  <section class="venue">
    <p class="venue-label">LOCATION</p>
    <p class="venue-address">HALVORN COMMUNITY CENTER,<br>241 PELLHAM STREET, PORTLAND,<br>ME 04102</p>
  </section>

  <footer class="contact">
    <span class="contact-item contact-phone">207-555-0148</span>
    <span class="contact-item contact-email">contact@brookmeadow.example</span>
    <span class="contact-item contact-web">www.vutel.example</span>
  </footer>
</main>
</body>
</html>
```